Business Card Design For A Cajun Seafood Restaurant

We are opening a cajun seafood restaurant in a week. We mainly serve cajun seafood which is orginally from Louisiana. We want design on both sides of a business card. I have menu on the website. You can go to www.bayourelish.com to check out our menu.

Restaurant name: Bayou Relish
Phone: +1 (818) 555-4172
Address: 48627 Dellmont Row, #5, Fernbrook, Ca90817
Email: bayourelish@mailbox.example
Website: www.bayourelish.com

Maybe add social media icons (facebook, instagram) if looks nice on the business card.
facebook.com/bayourelish
instagram.com/bayourelish or @bayourelish

Attached is the logo and other business card samples that I like.

```html
<!DOCTYPE html>
<html lang="en">
<head>
<meta charset="utf-8">
<title>Bayou Relish – Business Card</title>
<link href="https://fonts.googleapis.com/css2?family=Lato:wght@400;700;900&display=swap" rel="stylesheet">
<style>
  :root {
    --stage: #242424;
    --ink: #0b0b0b;
    --orange: #ec6a20;
    --orange-deep: #d4501a;
    --gold: #f5b400;
    --white: #ffffff;
    --rule: #e39a1c;
  }
  * { margin: 0; padding: 0; box-sizing: border-box; }
  html, body { width: 1200px; height: 1076px; overflow: hidden; }
  body {
    background: var(--stage);
    font-family: 'Lato', sans-serif;
    position: relative;
  }
  .card {
    position: absolute;
    left: 160px;
    width: 880px;
    height: 500px;
    overflow: hidden;
    box-shadow: 0 6px 18px rgba(0,0,0,.55);
  }

  /* ---------- Back side ---------- */
  .card-back { top: 25px; background: var(--ink); }
  .card-back .backdrop {
    position: absolute; inset: 0;
    background: radial-gradient(ellipse at 55% 45%, #2a1e17 0%, #17110d 45%, #0b0b0b 85%);
  }
  .card-back .brand {
    position: absolute; left: 0; right: 0; top: 150px;
    text-align: center;
  }
  .brand-name {
    font-weight: 900;
    font-size: 64px;
    line-height: 1.1;
    letter-spacing: 3px;
    color: var(--orange);
    text-transform: uppercase;
    white-space: nowrap;
  }
  .brand-tagline {
    display: inline-block;
    margin-top: 14px;
    background: var(--white);
    color: var(--ink);
    font-weight: 700;
    font-size: 22px;
    letter-spacing: 1.5px;
    padding: 6px 26px;
    text-transform: uppercase;
    white-space: nowrap;
  }
  .card-back .address {
    position: absolute; left: 0; right: 0; top: 400px;
    text-align: center;
    color: var(--white);
    font-size: 24px;
  }

  /* ---------- Front side ---------- */
  .card-front { top: 550px; background: var(--ink); }
  .front-header {
    position: absolute; left: 0; top: 0; width: 100%; height: 185px;
    background: linear-gradient(100deg, var(--orange-deep) 0%, var(--orange) 50%, #e25a1c 100%);
  }
  .front-header .brand {
    position: absolute; left: 34px; top: 48px; width: 500px; text-align: center;
  }
  .front-header .brand-name { color: var(--gold); font-size: 44px; }
  .front-header .brand-tagline { font-size: 19px; margin-top: 8px; }
  .contact-person {
    position: absolute; right: 0; top: 45px;
    width: 290px; height: 92px;
    background: var(--ink);
    border: 2px solid var(--white);
    border-right: none;
    border-radius: 10px 0 0 10px;
    text-align: right;
    padding: 12px 30px 0 0;
  }
  .person-name { color: var(--white); font-size: 32px; font-weight: 700; line-height: 1.05; white-space: nowrap; }
  .person-role { color: var(--orange); font-size: 25px; line-height: 1.2; white-space: nowrap; }

  .photo-strip {
    position: absolute; left: 0; top: 193px; width: 100%; height: 215px;
    background: var(--white);
    display: flex; gap: 6px; padding: 4px 0;
  }
  .photo { flex: 1; }
  .photo-platter { background: linear-gradient(135deg, #f3e6d8, #d98a5a 55%, #f0efe9); }
  .photo-taco { background: linear-gradient(135deg, #e8e2c8, #c9473a 50%, #d9c79a); }
  .photo-fish { background: linear-gradient(135deg, #e59a3a, #9a4a1d 55%, #c66a24); }
  .photo-lobster { background: linear-gradient(135deg, #c2331c, #e0572c 50%, #5f7a3a); }
  .gold-rule {
    position: absolute; left: 0; top: 408px; width: 100%; height: 6px;
    background: var(--rule);
  }
  .contact-bar {
    position: absolute; left: 0; top: 414px; width: 100%; height: 86px;
    display: flex; align-items: center; justify-content: center;
    font-size: 20px; color: var(--orange);
    white-space: nowrap;
  }
  .contact-bar .label { color: var(--gold); font-weight: 700; }
  .contact-bar .sep { color: var(--gold); font-weight: 700; margin: 0 7px; }
</style>
</head>
<body>

<section class="card card-back">
  <div class="backdrop" role="img" aria-label="Dim photo of a seafood boil"></div>
  <div class="brand">
    <div class="brand-name">Bayou Relish</div>
    <div class="brand-tagline">Louisiana Boil Kitchen</div>
  </div>
  <p class="address">48627 Dellmont Row, #5, Fernbrook, Ca90817</p>
</section>

<section class="card card-front">
  <header class="front-header">
    <div class="brand">
      <div class="brand-name">Bayou Relish</div>
      <div class="brand-tagline">Louisiana Boil Kitchen</div>
    </div>
    <div class="contact-person">
      <div class="person-name">Dana Whitfield</div>
      <div class="person-role">Managing Director</div>
    </div>
  </header>

  <div class="photo-strip">
    <div class="photo photo-platter" role="img" aria-label="Seafood platter with shrimp and oysters"></div>
    <div class="photo photo-taco" role="img" aria-label="Seafood taco with tomato and cabbage"></div>
    <div class="photo photo-fish" role="img" aria-label="Spiced whole fish with chillies"></div>
    <div class="photo photo-lobster" role="img" aria-label="Boiled crawfish and lobster"></div>
  </div>
  <div class="gold-rule"></div>

  <footer class="contact-bar">
    <span class="label">P:&nbsp;</span><span>+1 (818) 555-4172</span>
    <span class="sep">|</span>
    <span class="label">E:&nbsp;</span><span>bayourelish@mailbox.example</span>
    <span class="sep">|</span>
    <span class="label">W:&nbsp;</span><span>www.bayourelish.com</span>
  </footer>
</section>

</body>
</html>
```